WordPress Site That Reviews Footwear

We need a wordpress web design for an affiliate site called TarnWisp. We review and do roundups on footwear products. The final design should be clean and mobile friendly. The site should be built with Gutenberg page builder. We like the design of https://petalharvin.com/.

Target Market(s)

USA

Industry/Entity Type

Footwear

Logo Text

TarnWisp

Number of Pages Required

4 page

Font styles to use
Serif
Sans Serif

Requirements
Must have
• Wordpress site
Blog post
Page
Categories
Homepage

```html
<!DOCTYPE html>
<html lang="en">
<head>
<meta charset="utf-8">
<title>TarnWisp — All About Boots</title>
<link href="https://fonts.googleapis.com/css2?family=Questrial&family=Open+Sans:wght@400;600;700&display=swap" rel="stylesheet">
<style>
:root{
  --ink:#1f1f1f;
  --text:#5a5a5a;
  --accent:#5b86b4;
  --accent-line:#6f93bd;
  --line:#dcdfe4;
  --faq-bg:#f4f5f7;
  --sky-top:#eef4fb;
  --sky-bottom:#c4d8ee;
  --footer:#2b2b2b;
  --footer-text:#d8d8d8;
  --white:#ffffff;
}
*{box-sizing:border-box;margin:0;padding:0}
html,body{width:1200px;height:4409px;overflow:hidden}
body{font-family:"Open Sans",Arial,sans-serif;color:var(--text);background:var(--white);position:relative}
.heading{font-family:"Questrial","Century Gothic",sans-serif;color:var(--ink);font-weight:400;text-transform:uppercase;letter-spacing:.5px}
.abs{position:absolute}
a{color:inherit;text-decoration:none}

/* header */
.site-header{position:absolute;top:0;left:0;width:1200px;height:106px;border-bottom:1px solid #cfcfcf}
.brand{position:absolute;left:111px;top:24px;font-family:"Open Sans",sans-serif;font-weight:700;font-size:36px;color:var(--ink);letter-spacing:.5px;display:flex;align-items:center;gap:12px}
.brand .mark{width:14px;height:14px;background:var(--ink)}
.top-nav{position:absolute;right:111px;top:44px;display:flex;gap:24px;font-size:14px;color:#333}
.top-nav .current{text-decoration:underline}
.cat-nav{position:absolute;top:106px;left:0;width:1200px;height:46px;display:flex;justify-content:space-between;align-items:center;padding:0 111px;font-size:14px;color:#222;font-weight:600}

/* hero */
.hero{position:absolute;top:152px;left:0;width:1200px;height:565px;background:linear-gradient(135deg,#6d6149 0%,#9a8a66 35%,#c7b48a 55%,#7e6a4d 75%,#3e3325 100%)}
.hero h1{position:absolute;left:655px;top:148px;font-family:"Questrial",sans-serif;font-weight:400;font-size:60px;color:var(--white)}
.hero p{position:absolute;left:655px;top:236px;width:430px;font-size:23px;line-height:34px;color:var(--white)}
.btn{display:inline-flex;align-items:center;justify-content:center;background:var(--accent);color:var(--white);font-weight:600;font-size:16px;letter-spacing:.5px;text-transform:uppercase}
.hero .btn{position:absolute;left:655px;top:332px;width:184px;height:59px}
.dots{position:absolute;left:573px;top:497px;display:flex;gap:5px}
.dots span{width:15px;height:15px;border-radius:50%;border:2px solid var(--white)}
.dots .on{background:var(--white)}

/* welcome */
.welcome h2{position:absolute;left:111px;top:790px;font-size:40px}
.welcome .copy{position:absolute;left:111px;top:858px;width:500px;font-size:14.5px;line-height:25px}
.welcome .copy p+p{margin-top:25px}
.welcome .btn{position:absolute;left:111px;top:1113px;width:146px;height:53px;font-size:15px}
.photo-frame{position:absolute;border-right:2px solid var(--ink);border-bottom:2px solid var(--ink)}
.welcome .photo{position:absolute;left:666px;top:801px;width:423px;height:380px;background:linear-gradient(160deg,#6f7076,#46505e 45%,#8a3f4a 70%,#7a5a3c)}

/* activities */
.activities{position:absolute;top:1275px;left:0;width:1200px;height:779px;background:linear-gradient(180deg,var(--sky-top) 0%,#dde8f5 45%,var(--sky-bottom) 100%)}
.activities h2{position:absolute;top:66px;left:0;width:1200px;text-align:center;font-size:42px;line-height:53px}
.activity{position:absolute;width:205px;text-align:center}
.activity .ring{width:205px;height:205px;border-radius:50%;background:var(--white);border:1px solid #b9c6d6;display:flex;align-items:center;justify-content:center}
.activity .icon{width:110px;height:110px;border-radius:50%;background:#dbe5f1}
.activity .label{margin-top:10px;font-size:21px;color:#333}

/* choose */
.choose h2{position:absolute;top:2117px;left:0;width:1200px;text-align:center;font-size:42px}
.pick{position:absolute;top:2205px;width:228px;height:294px}
.pick .caption{position:absolute;left:0;bottom:22px;width:100%;text-align:center;color:var(--white);font-size:19px;line-height:24px;font-weight:600}
.slide-arrow{position:absolute;top:2331px;width:41px;height:41px;border:1px solid #555;border-radius:50%;display:flex;align-items:center;justify-content:center}

/* faq */
.faq{position:absolute;top:2573px;left:0;width:1200px;height:837px;background:var(--faq-bg)}
.faq h2{position:absolute;top:52px;left:0;width:1200px;text-align:center;font-size:42px}
.faq-item{position:absolute;left:111px;width:978px;background:var(--white);border:1px solid var(--line);border-radius:3px}
.faq-item .q{position:absolute;left:16px;top:16px;font-size:16.5px;font-weight:600;color:#333}
.faq-item .chev{position:absolute;right:16px;top:12px;width:32px;height:32px;border-radius:50%;background:#cdd6e2;display:flex;align-items:center;justify-content:center}
.faq-item .a{position:absolute;left:20px;top:52px;width:880px;font-size:14.5px;line-height:23px;color:#5a5a5a}
.faq-item .a p+p{margin-top:23px}

/* blog */
.blog h2{position:absolute;top:3478px;left:0;width:1200px;text-align:center;font-size:40px}
.post{position:absolute;top:3571px;width:300px}
.post .thumb{width:300px;height:243px}
.post h3{margin-top:40px;font-size:19px;line-height:27px;font-weight:400;color:#222}
.post .date{margin-top:6px;font-size:13px;color:#777;display:flex;align-items:center;gap:4px}

/* footer */
.site-footer{position:absolute;top:3997px;left:0;width:1200px;height:412px;background:var(--footer);color:var(--footer-text)}
.site-footer .brand{top:84px;color:var(--white);font-size:42px}
.site-footer .brand .mark{background:var(--white);width:16px;height:16px}
.foot-col{position:absolute;top:58px}
.foot-col h4{font-size:20px;font-weight:600;color:var(--white);margin-bottom:12px}
.foot-col li{list-style:none;font-size:15px;line-height:28px}
.foot-rule{position:absolute;left:111px;top:323px;width:978px;height:1px;background:#4a4a4a}
.copyright{position:absolute;left:111px;top:356px;font-size:15px;color:var(--white)}
.social{position:absolute;top:345px;display:flex;gap:9px;right:111px}
.social span{width:42px;height:42px;border:1.5px solid var(--white);border-radius:50%;display:block}
</style>
</head>
<body>

<header class="site-header">
  <a class="brand" href="#"><span class="mark"></span>TarnWisp</a>
  <nav class="top-nav"><a class="current" href="#">Home</a><a href="#">About</a><a href="#">Blog</a><a href="#">Contact</a></nav>
</header>
<nav class="cat-nav">
  <a href="#">Best Hiking Boots</a><a href="#">Best Combat Boots</a><a href="#">Best Work Boots</a><a href="#">Best Walking Shoes</a><a href="#">Best Hiking Gear</a><a href="#">Various Footwear</a><a href="#">Sports</a>
</nav>

<section class="hero" role="img" aria-label="Hiker's leather boots on a rocky mountain trail at sunset">
  <h1>All About Boots</h1>
  <p>Where We Take Outdoor Footwear Very Seriously!</p>
  <a class="btn" href="#">Get More Info</a>
  <div class="dots"><span class="on"></span><span></span><span></span></div>
</section>

<section class="welcome">
  <h2 class="heading">Welcome to TarnWisp</h2>
  <div class="copy">
    <p>Do you think all footwear is created alike? Think again! Hiking boots are a completely different beast than your average walking shoes.</p>
    <p>I have learned the importance of good footwear many years ago, when I gave myself plantar fasciitis by walking around on worn down budget boots for too long. I've gone through weeks of pure agony with every second I was standing up straight (which was most of the day).</p>
  </div>
  <a class="btn" href="#">Read More</a>
  <div class="photo-frame" style="left:719px;top:866px;width:387px;height:336px"></div>
  <div class="photo" role="img" aria-label="Two people seated on a patterned blanket wearing boots"></div>
</section>

<section class="activities">
  <h2 class="heading">Expert Footwear Advice,<br>Based on Activities</h2>
  <div class="activity" style="left:111px;top:207px"><div class="ring"><div class="icon" role="img" aria-label="Hiking pictogram"></div></div><div class="label">Hiking</div></div>
  <div class="activity" style="left:368px;top:207px"><div class="ring"><div class="icon" role="img" aria-label="Combat pictogram"></div></div><div class="label">Combat</div></div>
  <div class="activity" style="left:625px;top:207px"><div class="ring"><div class="icon" role="img" aria-label="Work pictogram"></div></div><div class="label">Work</div></div>
  <div class="activity" style="left:882px;top:207px"><div class="ring"><div class="icon" role="img" aria-label="Walking pictogram"></div></div><div class="label">Walking</div></div>
  <div class="activity" style="left:240px;top:455px"><div class="ring"><div class="icon" role="img" aria-label="Backpack pictogram"></div></div><div class="label">Hiking Gear</div></div>
  <div class="activity" style="left:497px;top:455px"><div class="ring"><div class="icon" role="img" aria-label="Boot pictogram"></div></div><div class="label">Various Footwear</div></div>
  <div class="activity" style="left:754px;top:455px"><div class="ring"><div class="icon" role="img" aria-label="Sports pictogram"></div></div><div class="label">Sports</div></div>
</section>

<section class="choose">
  <h2 class="heading">Choose the Best That Fit for You</h2>
  <a class="slide-arrow" style="left:47px" href="#" aria-label="Previous"><svg width="12" height="16" viewBox="0 0 12 16"><path d="M9 2 3 8l6 6" fill="none" stroke="#333" stroke-width="2"/></svg></a>
  <div class="pick" style="left:111px;background:linear-gradient(180deg,#d9c9a8,#6c5a58 55%,#2e2a2c)" role="img" aria-label="Woman stretching outdoors"><div class="caption">Shoes For<br>Overweight Women</div></div>
  <div class="pick" style="left:361px;background:linear-gradient(180deg,#7c8ea6,#3f4f6a 45%,#4a4a4a)" role="img" aria-label="Man jogging on a road"><div class="caption">Shoes For<br>Overweight men</div></div>
  <div class="pick" style="left:611px;background:linear-gradient(180deg,#4a453f,#2b2a28 60%,#1a1a1a)" role="img" aria-label="Lacing up a hiking boot"><div class="caption">Hiking Boots For Wide,<br>Narrow, Flat Feet</div></div>
  <div class="pick" style="left:861px;background:linear-gradient(180deg,#5e6b7a,#d06a2a 35%,#2e2e30 75%)" role="img" aria-label="Foot with highlighted heel pain"><div class="caption">Larkfield Plantar<br>Fasciitis Shoes</div></div>
  <a class="slide-arrow" style="left:1112px" href="#" aria-label="Next"><svg width="12" height="16" viewBox="0 0 12 16"><path d="m3 2 6 6-6 6" fill="none" stroke="#333" stroke-width="2"/></svg></a>
</section>

<section class="faq">
  <h2 class="heading">Frequently Asked Questions</h2>
  <div class="faq-item" style="top:149px;height:260px">
    <div class="q">Are My Boots Worn Out?</div>
    <div class="chev"><svg width="14" height="10" viewBox="0 0 14 10"><path d="m2 8 5-5 5 5" fill="none" stroke="#fff" stroke-width="2"/></svg></div>
    <div class="a">
      <p>Now matter how well made your black/brown rubber/leather boots are, eventually they will wear out. Once a boot starts showing its first signs of wear and tear, you can extend its lifespan by having it properly patched and/or repaired. Be sure to be in time with this, because once wear and tear starts setting in too heavily, there is nothing you can do to save that shoe anymore.</p>
      <p>Worn shoes are about the worst thing you can do to yourself. They will not provide you with proper support and you'll get tired sooner because of this. It's very bad for you, especially if you are a young person and your body is still developing.</p>
    </div>
  </div>
  <div class="faq-item" style="top:423px;height:57px"><div class="q">Are My Boots The Right Kind For My Activities Of Choice?</div><div class="chev"><svg width="14" height="10" viewBox="0 0 14 10"><path d="m2 2 5 5 5-5" fill="none" stroke="#fff" stroke-width="2"/></svg></div></div>
  <div class="faq-item" style="top:495px;height:57px"><div class="q">Do My Boots Have The Proper Width For My Feet?</div><div class="chev"><svg width="14" height="10" viewBox="0 0 14 10"><path d="m2 2 5 5 5-5" fill="none" stroke="#fff" stroke-width="2"/></svg></div></div>
  <div class="faq-item" style="top:566px;height:57px"><div class="q">Do My Boots Have The Proper Length For My Feet?</div><div class="chev"><svg width="14" height="10" viewBox="0 0 14 10"><path d="m2 2 5 5 5-5" fill="none" stroke="#fff" stroke-width="2"/></svg></div></div>
  <div class="faq-item" style="top:638px;height:57px"><div class="q">Do My Boots Accomodate My Toes Well Enough?</div><div class="chev"><svg width="14" height="10" viewBox="0 0 14 10"><path d="m2 2 5 5 5-5" fill="none" stroke="#fff" stroke-width="2"/></svg></div></div>
  <div class="faq-item" style="top:710px;height:57px"><div class="q">Do My Boots Give Me The Support I Need?</div><div class="chev"><svg width="14" height="10" viewBox="0 0 14 10"><path d="m2 2 5 5 5-5" fill="none" stroke="#fff" stroke-width="2"/></svg></div></div>
</section>

<section class="blog">
  <h2 class="heading">Blog</h2>
  <div class="photo-frame" style="left:134px;top:3600px;width:284px;height:221px"></div>
  <div class="photo-frame" style="left:470px;top:3600px;width:283px;height:221px"></div>
  <div class="photo-frame" style="left:804px;top:3600px;width:283px;height:221px"></div>
  <article class="post" style="left:111px">
    <div class="thumb" role="img" aria-label="Toddler wearing striped trousers and sneakers" style="background:linear-gradient(160deg,#6c7db8,#8b8d95 55%,#a9a9ab)"></div>
    <h3>Best Toddler Shoes for Kids who are Learning to Walk</h3>
    <div class="date"><svg width="13" height="13" viewBox="0 0 13 13"><rect x="1" y="2" width="11" height="10" fill="none" stroke="#888" stroke-width="1.2"/><path d="M1 5h11" stroke="#888" stroke-width="1.2"/></svg>July 6, 2021</div>
  </article>
  <article class="post" style="left:447px">
    <div class="thumb" role="img" aria-label="Athlete in training shoes mid-stride in a gym" style="background:linear-gradient(160deg,#7a7d82,#4b4d52 50%,#9a9b9f)"></div>
    <h3>Best Boxfit Shoes For Women For Comfort and Stability</h3>
    <div class="date"><svg width="13" height="13" viewBox="0 0 13 13"><rect x="1" y="2" width="11" height="10" fill="none" stroke="#888" stroke-width="1.2"/><path d="M1 5h11" stroke="#888" stroke-width="1.2"/></svg>July 6, 2021</div>
  </article>
  <article class="post" style="left:781px">
    <div class="thumb" role="img" aria-label="Tall brown leather boots in a dry field" style="background:linear-gradient(160deg,#c9b28c,#8a4f2e 45%,#b59a72)"></div>
    <h3>Best Over the Knee Boots to Rock Any Outfit in Style</h3>
    <div class="date"><svg width="13" height="13" viewBox="0 0 13 13"><rect x="1" y="2" width="11" height="10" fill="none" stroke="#888" stroke-width="1.2"/><path d="M1 5h11" stroke="#888" stroke-width="1.2"/></svg>July 6, 2021</div>
  </article>
</section>

<footer class="site-footer">
  <a class="brand" href="#"><span class="mark"></span>TarnWisp</a>
  <div class="foot-col" style="left:461px"><h4>Quick Links</h4><ul><li>Home</li><li>About</li><li>Blog post</li><li>Page</li><li>Categories</li><li>Contact</li></ul></div>
  <div class="foot-col" style="left:659px"><h4>Discover</h4><ul><li>Best Hiking Boots</li><li>Best Combat Boots</li><li>Best Work Boots</li><li>Best Walking Shoes</li><li>Best Hiking Gear</li><li>Various Footwear</li><li>Sports</li></ul></div>
  <div class="foot-col" style="left:907px"><h4>Company</h4><ul><li>Privacy Policy</li><li>Disclaimer</li></ul></div>
  <div class="foot-rule"></div>
  <div class="copyright">© 2021, TarnWisp. All rights reserved.</div>
  <div class="social"><span aria-label="Social link"></span><span aria-label="Social link"></span><span aria-label="Social link"></span></div>
</footer>

</body>
</html>
```